training for sustainable materials practice

Need design of a business card (later to be completed by letterhead and webdesign in same fashion) for a professional who works in the field of capacity building of professionals in mostly developing countries in the field waste/resource management, waste prevention/reduction, cleaner production, stakeholders involvement, etc.
Info on business cards is to include provided logo, info in provided file and picture.

Industry/Entity Type

Business

Contact Information for Business Card

White background

Font styles to use
Sans Serif

Colors

Designer to choose colors to be used in the design.

```html
<!DOCTYPE html>
<html lang="en">
<head>
<meta charset="utf-8">
<title>Greenfield Skills business card</title>
<link rel="stylesheet" href="https://fonts.googleapis.com/css2?family=Quicksand:wght@500;700&display=swap">
<style>
  :root {
    --page-bg: #ececec;
    --card-bg: #ffffff;
    --brand-green: #2f8a35;
    --soft-green: #d3e3cc;
    --icon-green: #cfe0c8;
    --ink: #1c1c1c;
    --photo-light: #9fb38f;
    --photo-dark: #4a5a42;
  }
  * { box-sizing: border-box; margin: 0; padding: 0; }
  html, body {
    width: 1200px; height: 800px; overflow: hidden;
    background: var(--page-bg);
    font-family: "Quicksand", sans-serif;
    color: var(--ink);
  }
  .business-card {
    position: absolute; left: 150px; top: 150px;
    width: 900px; height: 500px;
    background: var(--card-bg);
    overflow: hidden;
    box-shadow: 0 18px 40px rgba(0,0,0,0.12);
  }
  .card-art { position: absolute; inset: 0; width: 900px; height: 500px; }
  .brand {
    position: absolute; left: 62px; top: 52px;
    display: flex; align-items: center; gap: 14px;
  }
  .brand-mark { width: 30px; height: 30px; border-radius: 50%; background: var(--brand-green); }
  .brand-name {
    font-size: 42px; font-weight: 700; color: var(--brand-green);
    line-height: 1;
  }
  .brand-tagline {
    position: absolute; left: 108px; top: 104px;
    font-size: 13px; font-weight: 700; color: var(--brand-green);
  }
  .contact-list { position: absolute; left: 62px; top: 160px; list-style: none; }
  .contact-row { display: flex; align-items: flex-start; gap: 22px; margin-bottom: 18px; }
  .contact-icon {
    flex: none; width: 44px; height: 44px; border-radius: 50%;
    background: var(--icon-green);
    display: flex; align-items: center; justify-content: center;
  }
  .contact-icon svg { width: 22px; height: 22px; fill: #fff; stroke: #fff; }
  .contact-text { font-size: 18px; font-weight: 500; line-height: 1.2; padding-top: 10px; }
  .contact-text.person-name { font-size: 21px; font-weight: 700; padding-top: 9px; }
  .contact-text.online { padding-top: 2px; }
</style>
</head>
<body>
  <div class="business-card">
    <svg class="card-art" viewBox="0 0 900 500">
      <defs>
        <linearGradient id="portrait-tone" x1="0" y1="0" x2="1" y2="1">
          <stop offset="0" stop-color="#b7c2b0"/>
          <stop offset="0.5" stop-color="var(--photo-light)"/>
          <stop offset="1" stop-color="var(--photo-dark)"/>
        </linearGradient>
      </defs>
      <path class="accent-curve" d="M600 0 C 470 120, 470 380, 560 500 L900 500 L900 0 Z" fill="var(--soft-green)"/>
      <path class="portrait-area" role="img" aria-label="Portrait photo of the consultant in a white shirt in front of a window with green trees" d="M605 0 C 535 150, 560 380, 700 500 L900 500 L900 0 Z" fill="url(#portrait-tone)"/>
    </svg>

    <div class="brand">
      <span class="brand-mark"></span>
      <span class="brand-name">Greenfield Skills</span>
    </div>
    <div class="brand-tagline">training for sustainable materials practice</div>

    <ul class="contact-list">
      <li class="contact-row">
        <span class="contact-icon"><svg viewBox="0 0 24 24"><circle cx="12" cy="8" r="4.5" stroke="none"/><path d="M3.5 21c0-5 4-7.5 8.5-7.5s8.5 2.5 8.5 7.5z" stroke="none"/></svg></span>
        <span class="contact-text person-name">Jorin Vandemeer</span>
      </li>
      <li class="contact-row">
        <span class="contact-icon"><svg viewBox="0 0 24 24"><path d="M7 3.5l3 4-2 2c1 2.5 3 4.5 5.5 5.5l2-2 4 3-2 3c-7 0-14-7-14-14z" stroke="none"/></svg></span>
        <span class="contact-text">+49 1500 555 0142</span>
      </li>
      <li class="contact-row">
        <span class="contact-icon"><svg viewBox="0 0 24 24"><path d="M12 3 2 12h3v8h5v-5h4v5h5v-8h3z" stroke="none"/></svg></span>
        <span class="contact-text">Lindenhofweg 12<br>10117 Berlin, Deutschland</span>
      </li>
      <li class="contact-row">
        <span class="contact-icon"><svg viewBox="0 0 24 24"><g fill="none" stroke-width="1.6"><circle cx="12" cy="12" r="8.5"/><ellipse cx="12" cy="12" rx="3.8" ry="8.5"/><path d="M3.5 12h17M5 7.5h14M5 16.5h14"/></g></svg></span>
        <span class="contact-text online">jorin.vandemeer@greenfieldskills.org<br>www.greenfieldskills.org<br>Twitter: @jorinvandemeer<br>Skype: jvmeer2011<br>LinkedIn: Jorin Vandemeer</span>
      </li>
    </ul>
  </div>
</body>
</html>
```